Fernbrook premium pontoon cleaning and maintenance needs a business card design

we need a business card for a new company based in Brisbane and gold coast that offers to clean peoples pontoons using high pressure washers. The company name will be Fernbrook, and will offer premium pontoon cleaning and maintenance.
colours that can be used maybe black, lime green, grey, blue.but up for anything. cheers

Target Market(s)

people who own pontoons

Industry/Entity Type

Business

Contact Information for Business Card

contact
Rob Casworth
Duncan Pryle
mobile 0461 728 392
email Fernbrook@mailvista.net

Requirements
Nice to have
• like the look of black business cards the best

```html
<!DOCTYPE html>
<html lang="en">
<head>
<meta charset="utf-8">
<title>Fernbrook – Business Card</title>
<link href="https://fonts.googleapis.com/css2?family=Lato:wght@300;400;900&display=swap" rel="stylesheet">
<style>
  :root {
    --stage: #3a3a3c;
    --card: #1b1b1c;
    --card-edge: #2a2a2b;
    --photo-dark: #1e1f20;
    --photo-mid: #3b3d3f;
    --photo-light: #55585a;
    --white: #f4f4f4;
    --soft: #d9d9d9;
  }
  * { box-sizing: border-box; margin: 0; padding: 0; }
  html, body { width: 1200px; height: 900px; overflow: hidden; }
  body {
    background: var(--stage);
    font-family: "Lato", Arial, sans-serif;
    color: var(--white);
    position: relative;
  }
  .card {
    position: absolute;
    left: 290px;
    width: 620px;
    height: 380px;
    background: var(--card);
    border: 1px solid var(--card-edge);
    box-shadow: 0 10px 30px rgba(0,0,0,.45);
    overflow: hidden;
  }
  .card--front { top: 50px; }
  .card--back { top: 470px; }

  .brand {
    position: absolute;
    text-align: center;
    line-height: 1;
  }
  .brand__name {
    display: block;
    font-weight: 900;
    color: var(--white);
    letter-spacing: -1px;
  }
  .brand__tagline {
    display: block;
    font-weight: 400;
    color: var(--white);
    letter-spacing: .2px;
  }
  .card--front .brand { left: 0; right: 0; top: 118px; }
  .card--front .brand__name { font-size: 92px; }
  .card--front .brand__tagline { font-size: 21px; margin-top: 12px; }

  .back-photo {
    position: absolute; inset: 0;
    background: linear-gradient(180deg, var(--photo-dark) 0%, var(--photo-mid) 38%, var(--photo-light) 55%, var(--photo-mid) 72%, var(--photo-dark) 100%);
    opacity: .55;
  }
  .card--back .brand { left: 250px; top: 48px; width: 340px; }
  .card--back .brand__name { font-size: 64px; }
  .card--back .brand__tagline { font-size: 15px; margin-top: 8px; }

  .contacts__names {
    position: absolute; left: 44px; top: 70px;
    font-size: 22px; font-weight: 300; line-height: 1.3;
  }
  .divider {
    position: absolute; left: 44px; top: 238px;
    width: 520px; height: 1px; background: var(--soft);
  }
  .contact-line {
    position: absolute;
    display: flex; align-items: center; gap: 10px;
    font-weight: 400;
  }
  .contact-line--phone { left: 44px; top: 256px; font-size: 18px; }
  .contact-line--email { right: 56px; top: 318px; font-size: 22px; }
  .contact-line svg { fill: none; stroke: var(--white); stroke-width: 1.5; }
</style>
</head>
<body>

<section class="card card--front" aria-label="Card front">
  <div class="brand">
    <span class="brand__name">Fernbrook</span>
    <span class="brand__tagline">PONTOON CLEANING AND MAINTENANCE</span>
  </div>
</section>

<section class="card card--back" aria-label="Card back">
  <div class="back-photo" role="img" aria-label="Faded monochrome photograph of a pontoon jetty over calm water"></div>

  <div class="contacts__names">
    <p>Rob Casworth</p>
    <p>Duncan Pryle</p>
  </div>

  <div class="brand">
    <span class="brand__name">Fernbrook</span>
    <span class="brand__tagline">PONTOON CLEANING AND MAINTENANCE</span>
  </div>

  <div class="divider"></div>

  <p class="contact-line contact-line--phone">
    <svg width="12" height="18" viewBox="0 0 12 18" aria-hidden="true">
      <rect x="1" y="1" width="10" height="16" rx="1.5"/>
      <line x1="3" y1="4" x2="9" y2="4"/>
      <line x1="3" y1="8" x2="9" y2="8"/>
      <line x1="3" y1="11" x2="9" y2="11"/>
      <line x1="3" y1="14" x2="9" y2="14"/>
    </svg>
    <span>0461 728 392</span>
  </p>

  <p class="contact-line contact-line--email">
    <svg width="20" height="14" viewBox="0 0 20 14" aria-hidden="true">
      <rect x="1" y="1" width="18" height="12" fill="#f4f4f4"/>
      <polyline points="1,1 10,8 19,1" stroke="#1b1b1c"/>
    </svg>
    <span>Fernbrook@mailvista.net</span>
  </p>
</section>

</body>
</html>
```